Kit Darvell - health and fitness coach who needs a web page. simple and effective

I am a online health and fitness coach who runs a 10 week challenge 4 times a year. I am wanting, a menu with a bit about me, a place where people can buy the programme, testimonies, memberships, photos, and recipes.
I am wanting it to look modern, professional and simple.
The website is how potential clients can check out the memberships for the programme, photos of myself and and my family to show members that I am a confident, educated, independent and healthy woman. Who is very passionate about making a difference in people lives to become a better version of themselves.
My training philosophy is simple, Commitment to training, Consistently working hard and training equals Change! Change is physical changes to the body!!

Target Market(s)

Woman 25-44 years

Industry/Entity Type

Health And Wellness

Coding

Coded - Design and coding required

Number of Pages Required

5+ page

Font styles to use
Sans Serif

Colors
fbed22
e667a6
ffffff

Requirements
Must have
• I like the style of "plain tile" website design.
• On the menu bar I want 9 different tabs/options to click on, these are named:
• BLOG
• ABOUT
• TRAINING PROGRAMS
• HEALTHY FOOD
• SUBSCRIBE
• TESTIMONIALS
• CHATWALL
• SNAPLOOMER
• VID REEL
Nice to have
• logo at the top (attached under file 2)
• Easy for myself to add information once website design is completed.
• lots of white space, white a bright yellow (same as logo) or pink
Should not have
• clutter

```html
<!DOCTYPE html>
<html lang="en">
<head>
<meta charset="utf-8">
<title>Kit Darvell – Fitness, Health, Lifestyle</title>
<link href="https://fonts.googleapis.com/css2?family=Raleway:ital,wght@0,500;0,600;0,700;1,500&family=Lato:ital,wght@0,400;0,700;1,400;1,700&display=swap" rel="stylesheet">
<style>
:root{
  --yellow:#fbed22;
  --pink:#e667a6;
  --white:#ffffff;
  --ink:#333333;
  --muted:#666666;
  --dark:#1f1f1f;
  --band:#2b2b2b;
  --light:#f1f1f1;
}
*{box-sizing:border-box;margin:0;padding:0}
html,body{width:1200px;height:3782px;overflow:hidden}
body{position:relative;background:var(--white);font-family:"Lato",Arial,sans-serif;color:var(--ink)}
.abs{position:absolute}
.heading{font-family:"Raleway",Arial,sans-serif;font-weight:600;font-size:36px}
.heading .rule{display:inline-block;width:80px;height:2px;background:currentColor;vertical-align:middle;margin-left:24px;opacity:.6}
.btn{position:absolute;background:var(--yellow);color:var(--ink);font-family:"Lato",Arial,sans-serif;font-size:18px;text-transform:uppercase;border-radius:30px;display:flex;align-items:center;justify-content:center;box-shadow:0 4px 0 var(--pink)}
.ph{position:absolute}
.arrow{position:absolute;width:52px;height:52px;border-radius:50%;display:flex;align-items:center;justify-content:center}

/* header */
.brand{left:80px;top:28px;display:flex;align-items:center;gap:14px}
.brand .mark{width:74px;height:74px;border-radius:50%;background:var(--yellow)}
.brand .name{font-family:"Lato",Arial,sans-serif;font-size:34px;color:var(--yellow);font-weight:400;letter-spacing:1px;text-transform:uppercase;line-height:1}
.brand .tag{font-size:12px;color:var(--ink);margin-top:6px}
.contact-top{left:720px;top:36px;display:flex;align-items:center;gap:14px}
.contact-top .icon{width:58px;height:58px;border-radius:50%;background:var(--yellow);display:flex;align-items:center;justify-content:center}
.contact-top .phone{font-size:22px;color:var(--ink)}
.contact-top .mail{font-size:15px;color:var(--muted)}
.nav{left:0;top:136px;width:1200px;height:66px;background:var(--pink);display:flex;align-items:center;padding:0 80px;justify-content:space-between}
.nav a{color:var(--white);text-decoration:none;font-size:18px}

/* hero */
.hero{left:0;top:202px;width:1200px;height:580px;background:linear-gradient(120deg,#3a3a3a,#6b6b6b 45%,#2c2c2c)}
.hero-title{left:0;top:355px;width:1200px;text-align:center;color:var(--white);font-family:"Raleway",Arial,sans-serif;font-weight:700;font-size:50px}
.hero-sub{left:0;top:420px;width:1200px;text-align:center;color:var(--white);font-style:italic;font-size:30px;line-height:44px}

/* about */
.about-text{left:80px;top:920px;width:560px;font-size:14px;line-height:24px;color:var(--muted)}
.about-text p{margin-bottom:16px}
.circle{position:absolute;border-radius:50%;border:6px solid var(--white);box-shadow:0 2px 10px rgba(0,0,0,.15)}

/* foods */
.foods{left:0;top:1210px;width:1200px;height:385px;background:linear-gradient(90deg,#1e1e1e,#2f3a28 60%,#243022)}
.tile{position:absolute}

/* blog */
.post{position:absolute;left:80px;width:540px;height:160px}
.post .thumb{position:absolute;left:0;top:0;width:155px;height:120px}
.post h3{position:absolute;left:166px;top:0;font-family:"Raleway",Arial,sans-serif;font-weight:500;font-size:20px;color:var(--pink)}
.post .meta{position:absolute;left:166px;top:42px;font-size:12px;color:#888;font-style:italic}
.post .meta b{font-weight:400;margin:0 8px}
.post p{position:absolute;left:166px;top:72px;width:370px;font-size:14px;line-height:24px;color:var(--muted)}
.play{position:absolute;border-radius:50%;border:3px solid var(--white);display:flex;align-items:center;justify-content:center}

/* courses */
.courses{left:0;top:2465px;width:1200px;height:695px;background:linear-gradient(180deg,#3c3c3c,#5a5a5a 50%,#3a3a3a)}
.card{position:absolute;top:2608px;width:252px;height:378px;background:var(--white)}
.card .img{height:165px}
.card h4{margin:20px 18px 0;font-family:"Raleway",Arial,sans-serif;font-weight:600;font-size:17px;line-height:22px;color:var(--pink)}
.card .coach{position:absolute;left:18px;top:250px;display:flex;align-items:center;gap:10px;font-size:13px;line-height:16px}
.card .coach .av{width:34px;height:34px;background:#c9a08a}
.card .count{position:absolute;left:150px;top:258px;font-size:14px;color:var(--ink);display:flex;gap:8px;align-items:center}
.card .foot{position:absolute;left:0;top:312px;width:100%;border-top:1px solid #e5e5e5;display:flex;justify-content:space-between;padding:18px 18px 0}
.card .stars{color:#e0b400;font-size:13px;letter-spacing:1px}
.card .price{color:#2e9c3e;font-weight:700;font-size:20px}

/* stories */
.stories{left:0;top:3160px;width:1200px;height:355px;background:var(--pink)}
.story{position:absolute;top:3305px;width:440px;height:140px}
.story .avatar{position:absolute;left:0;top:0;width:110px;height:110px;border-radius:50%;background:#d9c6bd;border:5px solid var(--white)}
.story .quote{position:absolute;left:130px;top:0;color:var(--white)}
.story .quote h5{font-weight:700;font-style:italic;font-size:19px;display:flex;gap:8px;align-items:flex-start}
.story .quote h5 span{color:var(--yellow);font-size:40px;line-height:26px;font-family:Georgia,serif}
.story .quote p{font-size:14px;line-height:24px;margin-top:6px;width:320px}
.story .quote .who{font-style:italic;font-weight:700;font-size:14px;margin-top:6px}
.story .quote .role{font-style:italic;font-size:11px}

/* footer */
.foot-top{left:0;top:3515px;width:1200px;height:105px;background:linear-gradient(90deg,#ececec,#f5f5f5,#e9e9e9)}
.foot-contact{display:flex;align-items:center;gap:12px;font-size:16px;color:var(--ink)}
.social{position:absolute;width:36px;height:36px;border-radius:50%;border:2px solid var(--pink)}
.foot-links{left:350px;top:3672px;display:flex;gap:8px;font-size:14px;color:var(--ink)}
.copy{left:355px;top:3705px;font-size:14px;color:var(--ink)}
.strip{left:0;top:3765px;width:1200px;height:17px;background:var(--yellow)}
</style>
</head>
<body>

<!-- Header -->
<div class="abs brand">
  <div class="mark"></div>
  <div><div class="name">Kit Darvell</div><div class="tag">Fitness. Health. Lifestyle.</div></div>
</div>
<div class="abs contact-top">
  <div class="icon"><svg width="26" height="26" viewBox="0 0 24 24"><path fill="#e667a6" d="M6.6 10.8a15 15 0 0 0 6.6 6.6l2.2-2.2c.3-.3.7-.4 1-.2 1.1.4 2.3.6 3.6.6.6 0 1 .4 1 1V20c0 .6-.4 1-1 1A17 17 0 0 1 3 4c0-.6.4-1 1-1h3.5c.6 0 1 .4 1 1 0 1.3.2 2.5.6 3.6.1.3 0 .7-.2 1z"/></svg></div>
  <div><div class="phone">123-456-7890</div><div class="mail">info@kitdarvell.example</div></div>
</div>
<div class="btn" style="left:965px;top:40px;width:156px;height:54px;font-size:17px">Subscribe</div>

<nav class="abs nav">
  <a>Blog</a><a>About</a><a>Training Programs</a><a>Healthy Food</a><a>Subscribe</a><a>Testimonials</a><a>Chatwall</a><a>Snaploomer</a><a>Vid Reel</a>
</nav>

<!-- Hero -->
<div class="abs hero" role="img" aria-label="Coach and client training together in a gym"></div>
<div class="arrow" style="left:50px;top:408px;background:rgba(255,255,255,.35)"><svg width="18" height="18" viewBox="0 0 18 18"><path d="M12 3 6 9l6 6" stroke="#fff" stroke-width="2.5" fill="none"/></svg></div>
<div class="arrow" style="left:1092px;top:408px;background:var(--yellow)"><svg width="18" height="18" viewBox="0 0 18 18"><path d="M6 3l6 6-6 6" stroke="#333" stroke-width="2.5" fill="none"/></svg></div>
<div class="abs hero-title">Hii....I'M KIT DARVELL</div>
<div class="abs hero-sub">Discover the Secret of Living a Life with<br>Passion!</div>
<div class="btn" style="left:518px;top:535px;width:166px;height:58px">Contact Me</div>
<svg class="abs" style="left:0;top:640px" width="1200" height="145" viewBox="0 0 1200 145">
  <path d="M0 40 Q600 200 1200 20 L1200 145 L0 145Z" fill="#fff"/>
  <path d="M0 45 Q600 205 1200 25 L1200 40 Q600 215 0 70Z" fill="#e667a6"/>
  <path d="M0 70 Q600 215 1200 40" stroke="#fbed22" stroke-width="5" fill="none"/>
</svg>

<!-- About -->
<div class="abs heading" style="left:80px;top:848px;color:var(--pink)">About Me</div>
<div class="abs about-text">
  <p>Kit Darvell is Coach Kit. A health and fitness coach since 2008 after completing a Bachelor of Recreation and Sports at Harbourne University.</p>
  <p>Kit has been in the fitness industry for a number of years achieving high honours as one of New Zealanders top gym instructors and group exercise instructor of the year. She has trained many high performance athletes and the every day person.</p>
</div>
<div class="btn" style="left:80px;top:1087px;width:165px;height:54px">View Details</div>
<div class="circle" style="left:876px;top:895px;width:220px;height:220px;background:linear-gradient(135deg,#8a7a6a,#c4b3a0)" role="img" aria-label="Coach with a group of women after a workout"></div>
<div class="circle" style="left:680px;top:850px;width:290px;height:290px;background:linear-gradient(135deg,#6f7a80,#b8aaa0)" role="img" aria-label="Coach giving a thumbs up"></div>
<div class="play" style="left:800px;top:970px;width:56px;height:56px"><svg width="20" height="22" viewBox="0 0 20 22"><path d="M3 2l15 9-15 9z" fill="#fff"/></svg></div>

<!-- Healthy Foods -->
<div class="abs foods" role="img" aria-label="Dark background of fresh green food"></div>
<div class="abs heading" style="left:80px;top:1268px;color:var(--pink)">Healthy Foods<span class="rule" style="color:#fff"></span></div>
<div class="abs" style="left:80px;top:1355px;width:230px;font-size:14px;line-height:24px;color:var(--white)">Lorem Ipsum is simply dummy text of the printing and typesetting industry. Lorem Ipsum has been the dummy text ever since the 1500s.</div>
<div class="arrow" style="left:80px;top:1482px;width:40px;height:40px;border:2px solid #fff"><svg width="14" height="14" viewBox="0 0 18 18"><path d="M12 3 6 9l6 6" stroke="#fff" stroke-width="2.5" fill="none"/></svg></div>
<div class="arrow" style="left:130px;top:1482px;width:40px;height:40px;border:2px solid var(--yellow)"><svg width="14" height="14" viewBox="0 0 18 18"><path d="M6 3l6 6-6 6" stroke="#fbed22" stroke-width="2.5" fill="none"/></svg></div>
<div class="tile" style="left:333px;top:1355px;width:252px;height:165px;background:linear-gradient(135deg,#d8c7a6,#a9c36c 55%,#d46a3a)" role="img" aria-label="Dip with fresh vegetables"></div>
<div class="tile" style="left:598px;top:1355px;width:255px;height:165px;background:linear-gradient(135deg,#c79a6b,#8a4b3c 55%,#d9b48a)" role="img" aria-label="Homemade muffins"></div>
<div class="tile" style="left:866px;top:1355px;width:254px;height:165px;background:linear-gradient(135deg,#e9d9b0,#b5473b 50%,#6e9a3a)" role="img" aria-label="Salad with eggs and tomato"></div>

<!-- Blog -->
<div class="abs heading" style="left:80px;top:1655px;color:var(--pink)">Blog<span class="rule" style="color:#ccc"></span></div>
<div class="post" style="top:1745px">
  <div class="thumb" style="background:linear-gradient(180deg,#9fc4e0,#d9cbb2)" role="img" aria-label="Handstand on the beach"></div>
  <h3>Lorem Ipsum Dummy Text Printing.</h3>
  <div class="meta">By KIT<b>/</b>In Health &amp; Fitness<b>/</b>May 31, 2018</div>
  <p>Lorem Ipsum is simply dummy text of the printing and typesetting industry. Lorem Ipsum has been the print industry's standard dummy text ever since the 1500s.</p>
</div>
<div class="post" style="top:1945px">
  <div class="thumb" style="background:linear-gradient(180deg,#8a7b6a,#4a4540)" role="img" aria-label="Holding a fresh catch"></div>
  <h3>Lorem Ipsum Dummy Text Printing.</h3>
  <div class="meta">By KIT<b>/</b>In Health &amp; Fitness<b>/</b>May 31, 2018</div>
  <p>Lorem Ipsum is simply dummy text of the printing and typesetting industry. Lorem Ipsum has been the print industry's standard dummy text ever since the 1500s.</p>
</div>
<div class="post" style="top:2143px">
  <div class="thumb" style="background:linear-gradient(180deg,#bcc8d2,#6d7a5e)" role="img" aria-label="Running on a country road"></div>
  <h3>Lorem Ipsum Dummy Text Printing.</h3>
  <div class="meta">By KIT<b>/</b>In Health &amp; Fitness<b>/</b>May 31, 2018</div>
  <p>Lorem Ipsum is simply dummy text of the printing and typesetting industry. Lorem Ipsum has been the print industry's standard dummy text ever since the 1500s.</p>
</div>
<div class="btn" style="left:80px;top:2343px;width:142px;height:52px">View All</div>

<!-- Videos -->
<div class="abs heading" style="left:655px;top:1655px;color:var(--pink)">Videos<span class="rule" style="color:#ccc"></span></div>
<div class="ph" style="left:655px;top:1732px;width:466px;height:290px;background:linear-gradient(135deg,#2a2a2a,#5a5550 50%,#1f1f1f)" role="img" aria-label="Coach with a client in the gym"></div>
<div class="play" style="left:858px;top:1825px;width:60px;height:60px"><svg width="20" height="22" viewBox="0 0 20 22"><path d="M3 2l15 9-15 9z" fill="#fff"/></svg></div>
<div class="abs" style="left:678px;top:1930px;font-weight:700;font-size:18px;color:var(--yellow)">Introduction of Health &amp; Fitness</div>
<div class="abs" style="left:678px;top:1960px;font-size:13px;color:var(--white)">Lorem Ipsum dummy typesetting industry.</div>
<div class="ph" style="left:655px;top:2068px;width:214px;height:228px;background:linear-gradient(135deg,#8b6b55,#c9b6a0)" role="img" aria-label="Cooking a healthy meal"></div>
<div class="play" style="left:738px;top:2155px;width:50px;height:50px"><svg width="16" height="18" viewBox="0 0 20 22"><path d="M3 2l15 9-15 9z" fill="#fff"/></svg></div>
<div class="ph" style="left:907px;top:2068px;width:214px;height:228px;background:linear-gradient(135deg,#5d7a3e,#9aa870)" role="img" aria-label="Outdoor workout on the grass"></div>
<div class="play" style="left:990px;top:2155px;width:50px;height:50px"><svg width="16" height="18" viewBox="0 0 20 22"><path d="M3 2l15 9-15 9z" fill="#fff"/></svg></div>
<div class="btn" style="left:655px;top:2343px;width:146px;height:52px">View All</div>

<!-- Online Coaching Courses -->
<div class="abs courses" role="img" aria-label="Blurred gym equipment background"></div>
<div class="abs heading" style="left:80px;top:2520px;color:var(--yellow)">Online Coaching Courses<span class="rule" style="color:var(--yellow)"></span></div>
<div class="arrow" style="left:1028px;top:2522px;width:40px;height:40px;border:2px solid #fff"><svg width="14" height="14" viewBox="0 0 18 18"><path d="M12 3 6 9l6 6" stroke="#fff" stroke-width="2.5" fill="none"/></svg></div>
<div class="arrow" style="left:1080px;top:2522px;width:40px;height:40px;border:2px solid var(--yellow)"><svg width="14" height="14" viewBox="0 0 18 18"><path d="M6 3l6 6-6 6" stroke="#fbed22" stroke-width="2.5" fill="none"/></svg></div>

<div class="card" style="left:78px">
  <div class="img" style="background:linear-gradient(135deg,#7a7a74,#a9a89e)" role="img" aria-label="Lunge exercise"></div>
  <h4>Introduction of Health &amp; Fitness</h4>
  <div class="coach"><div class="av"></div><div>Kit<br>Darvell</div></div>
  <div class="count"><svg width="20" height="16" viewBox="0 0 20 16"><circle cx="7" cy="5" r="4" fill="#e667a6"/><circle cx="14" cy="5" r="3.5" fill="#e667a6"/><path d="M0 16c0-5 14-5 14 0zM10 16c0-4 10-5 10 0z" fill="#e667a6"/></svg>221</div>
  <div class="foot"><span class="stars">★★★★☆</span><span class="price">$140.00</span></div>
</div>
<div class="card" style="left:343px">
  <div class="img" style="background:linear-gradient(135deg,#4f5a3c,#8a8f7a)" role="img" aria-label="Flexing beside a truck"></div>
  <h4>Introduction of Health &amp; Fitness</h4>
  <div class="coach"><div class="av"></div><div>Kit<br>Darvell</div></div>
  <div class="count"><svg width="20" height="16" viewBox="0 0 20 16"><circle cx="7" cy="5" r="4" fill="#e667a6"/><circle cx="14" cy="5" r="3.5" fill="#e667a6"/><path d="M0 16c0-5 14-5 14 0zM10 16c0-4 10-5 10 0z" fill="#e667a6"/></svg>91</div>
  <div class="foot"><span class="stars">★★★★☆</span><span class="price">$40.00</span></div>
</div>
<div class="card" style="left:608px">
  <div class="img" style="background:linear-gradient(135deg,#5a5a5a,#b04a6a 50%,#3a3a3a)" role="img" aria-label="Group training class"></div>
  <h4>Introduction of Health &amp; Fitness</h4>
  <div class="coach"><div class="av"></div><div>Kit<br>Darvell</div></div>
  <div class="count"><svg width="20" height="16" viewBox="0 0 20 16"><circle cx="7" cy="5" r="4" fill="#e667a6"/><circle cx="14" cy="5" r="3.5" fill="#e667a6"/><path d="M0 16c0-5 14-5 14 0zM10 16c0-4 10-5 10 0z" fill="#e667a6"/></svg>101</div>
  <div class="foot"><span class="stars">★★★★☆</span><span class="price">$50.00</span></div>
</div>
<div class="card" style="left:872px">
  <div class="img" style="background:linear-gradient(180deg,#9a9a90,#2a2a2a)" role="img" aria-label="Squat exercise in the gym"></div>
  <h4>Introduction of Health &amp; Fitness</h4>
  <div class="coach"><div class="av"></div><div>Kit<br>Darvell</div></div>
  <div class="count"><svg width="20" height="16" viewBox="0 0 20 16"><circle cx="7" cy="5" r="4" fill="#e667a6"/><circle cx="14" cy="5" r="3.5" fill="#e667a6"/><path d="M0 16c0-5 14-5 14 0zM10 16c0-4 10-5 10 0z" fill="#e667a6"/></svg>154</div>
  <div class="foot"><span class="stars">★★★★☆</span><span class="price">Free</span></div>
</div>
<div class="btn" style="left:527px;top:3035px;width:146px;height:54px">View All</div>

<!-- Success Stories -->
<div class="abs stories"></div>
<div class="abs heading" style="left:80px;top:3218px;color:var(--yellow)">Success Stories<span class="rule" style="color:var(--yellow)"></span></div>
<div class="story" style="left:80px">
  <div class="avatar" role="img" aria-label="Client portrait"></div>
  <div class="quote">
    <h5><span>“</span>Lorem Ipsum typesetting industry.</h5>
    <p>Lorem Ipsum is simply dummy text of the printing and typesetting industry's standard dummy text ever since the 1500s.</p>
    <div class="who">- ANDREW</div><div class="role">Coach of fitness</div>
  </div>
</div>
<div class="story" style="left:620px">
  <div class="avatar" role="img" aria-label="Client portrait"></div>
  <div class="quote">
    <h5><span>“</span>Lorem Ipsum typesetting industry.</h5>
    <p>Lorem Ipsum is simply dummy text of the printing and typesetting industry's standard dummy text ever since the 1500s.</p>
    <div class="who">- ANDREW</div><div class="role">Coach of fitness</div>
  </div>
</div>
<div class="abs" style="left:1112px;top:3340px;width:14px;height:14px;border-radius:50%;border:2px solid #fff"></div>
<div class="abs" style="left:1112px;top:3362px;width:14px;height:14px;border-radius:50%;background:#fff"></div>
<div class="abs" style="left:1112px;top:3384px;width:14px;height:14px;border-radius:50%;border:2px solid #fff"></div>

<!-- Footer -->
<div class="abs foot-top" role="img" aria-label="Faint collage of training photos"></div>
<div class="abs foot-contact" style="left:80px;top:3557px">
  <svg width="20" height="20" viewBox="0 0 24 24"><path fill="#e667a6" d="M6.6 10.8a15 15 0 0 0 6.6 6.6l2.2-2.2c.3-.3.7-.4 1-.2 1.1.4 2.3.6 3.6.6.6 0 1 .4 1 1V20c0 .6-.4 1-1 1A17 17 0 0 1 3 4c0-.6.4-1 1-1h3.5c.6 0 1 .4 1 1 0 1.3.2 2.5.6 3.6.1.3 0 .7-.2 1z"/></svg>
  123-456-7890
</div>
<div class="abs foot-contact" style="left:242px;top:3557px">
  <svg width="22" height="16" viewBox="0 0 22 16"><rect x="1" y="1" width="20" height="14" fill="#e667a6"/><path d="M1 1l10 8 10-8" stroke="#fff" stroke-width="1.5" fill="none"/></svg>
  info@kitdarvell.example
</div>
<div class="social" style="left:858px;top:3548px"></div>
<div class="social" style="left:904px;top:3548px"></div>
<div class="social" style="left:950px;top:3548px"></div>
<div class="btn" style="left:1018px;top:3542px;width:104px;height:46px;font-size:17px">Login</div>

<div class="abs brand" style="top:3655px;gap:10px">
  <div class="mark" style="width:50px;height:50px"></div>
  <div><div class="name" style="font-size:26px">Kit Darvell</div><div class="tag" style="font-size:10px">Fitness. Health. Lifestyle.</div></div>
</div>
<div class="abs foot-links"><span>Blog</span>|<span>About</span>|<span>Training Programs</span>|<span>Healthy Food</span>|<span>Subscribe</span>|<span>Testimonial</span>|<span>Chatwall</span>|<span>Vid Reel</span>|<span>Snaploomer</span></div>
<div class="abs copy">Copyright © 2018 KIT DARVELL Pty Ltd. All Right Reserved.</div>
<div class="abs strip"></div>

</body>
</html>
```